Flyer für einen Sanitär Heizungs Betrieb
Zielgruppe
Sanitär Heizungs Betrieb der den Fokus verstärkt auf den Service an Heizungsanlagen setzten will.
Der Flyer soll sowohl an Privathaushalte als auch an Hausverwaltungen gehen.
Er soll unsere Leistungen aufzeigen und einen guten ersten Eindruck vermitteln.
Aufgabenstellung
Anbei sende ich Themen die als Leistung aufgeführt werden, sowie Strichwort für einen Werbetext (kann gerne generiert werden ansonsten kommt er noch zum texter)

```html
<!DOCTYPE html>
<html lang="de">
<head>
<meta charset="utf-8">
<title>Das sind wir – Flyer</title>
<link href="https://fonts.googleapis.com/css2?family=Open+Sans:wght@400;600;700&display=swap" rel="stylesheet">
<style>
  :root {
    --blue: #1b7bc6;
    --text: #3a3a3a;
    --text-strong: #1f1f1f;
    --yellow: #ffd21a;
    --footer-bg: #2b2b2d;
    --white: #ffffff;
  }
  * { margin: 0; padding: 0; box-sizing: border-box; }
  html, body { width: 847px; height: 1200px; overflow: hidden; background: var(--white); }
  .flyer {
    position: relative;
    width: 847px;
    height: 1200px;
    font-family: "Open Sans", Arial, sans-serif;
    color: var(--text);
    background: var(--white);
  }
  .intro {
    position: absolute;
    left: 65px;
    top: 30px;
    width: 717px;
  }
  .intro__title {
    font-size: 28px;
    font-weight: 700;
    color: var(--blue);
    letter-spacing: 0.3px;
    line-height: 1.2;
    margin-bottom: 23px;
  }
  .intro__text {
    font-size: 20.4px;
    line-height: 29.1px;
    text-align: justify;
    hyphens: auto;
    -webkit-hyphens: auto;
  }
  .intro__text strong {
    font-weight: 600;
    color: var(--text-strong);
  }
  .gallery {
    position: absolute;
    left: 0;
    top: 534px;
    width: 847px;
    height: 427px;
    background: var(--yellow);
  }
  .gallery__photo {
    position: absolute;
    top: 6px;
    height: 413px;
  }
  .gallery__photo--house {
    left: 0;
    width: 418px;
    background: linear-gradient(180deg, #c9ccce 0%, #b8bcbf 25%, #2a2a2c 26%, #1e1e20 70%, #8a6a4c 72%, #9a9a98 88%, #7d8a6e 100%);
  }
  .gallery__photo--bath {
    left: 423px;
    width: 424px;
    background: linear-gradient(180deg, #f3f3f2 0%, #ececea 55%, #e8dccc 70%, #d2ab7c 85%, #c89b6a 100%);
  }
  .gallery__gap {
    position: absolute;
    left: 418px;
    top: 6px;
    width: 5px;
    height: 413px;
    background: var(--white);
  }
  .contact {
    position: absolute;
    left: 0;
    top: 961px;
    width: 847px;
    height: 239px;
    background: var(--footer-bg);
    color: var(--white);
  }
  .contact__site {
    position: absolute;
    top: 38px;
    font-size: 21.5px;
    line-height: 26.8px;
    font-style: normal;
  }
  .contact__site--esslingen { left: 33px; }
  .contact__site--weil { left: 449px; }
  .contact__name { font-weight: 600; display: block; }
</style>
</head>
<body>
  <main class="flyer">
    <section class="intro">
      <h1 class="intro__title">DAS SIND WIR</h1>
      <p class="intro__text">Herzlich willkommen bei unserem Familienunternehmen im Kreis Böblingen, das im Jahr 2023 stolz sein 20-jähriges Jubiläum feiert! Unsere <strong>geschulten Fachkräfte</strong> stehen für eine Vielzahl von Leistungen bereit, darunter Wartung von Zentralheizungen, Reparaturen von Heizungs- und Sanitäranlagen, Solaranlagenservice und vieles mehr. Wir legen großen Wert auf <strong>gewissenhaftes und zielorientiertes Arbeiten</strong>, und als eingetragener Meisterbetrieb der Innung Stuttgart garantieren wir <strong>höchste Qualität</strong>. Als Ausbildungsbetrieb sind wir stets bestrebt, Fach&shy;kompetenz und Innovation zu fördern. Mit <strong>langjähriger Erfahrung</strong> im Umgang mit Privathaushalten und Hausverwaltungen bieten wir Ihnen zuverlässige Dienstleistungen und einen <strong>erstklassigen Service</strong>. Vertrau&shy;en Sie auf unser Engagement für Ihre Heizungs- und Sanitäranliegen – wir freuen uns darauf, <strong>Sie persönlich</strong> betreuen zu dürfen.</p>
    </section>

    <section class="gallery">
      <div class="gallery__photo gallery__photo--house" role="img" aria-label="Foto: modernes dunkles Holzhaus mit Wärmepumpe vor dem Eingang"></div>
      <div class="gallery__gap"></div>
      <div class="gallery__photo gallery__photo--bath" role="img" aria-label="Foto: helles Badezimmer mit freistehender Badewanne, rundem Spiegel und Holzboden"></div>
    </section>

    <footer class="contact">
      <address class="contact__site contact__site--esslingen">
        <span class="contact__name">Standort Esslingen am Neckar</span>
        Brunnenstraße 12<br>
        73734 Esslingen am Neckar<br>
        (0711) 48 26 19 3<br>
        info@wkrgmbh.de
      </address>
      <address class="contact__site contact__site--weil">
        <span class="contact__name">Standort Weil im Schönbuch</span>
        Birkenweg 8<br>
        73734 Esslingen am Neckar<br>
        (07157) 41 28 6<br>
        (07031) 58 34 17<br>
        info@wkrgmbh.de
      </address>
    </footer>
  </main>
</body>
</html>
```